BrightPlacely.com Wordpress Theme

Hi,

I am looking for a new theme for my wordpress site. The site looks average at the moment and needs a boost. I want to have a better user experience for publishers and advertisers and the proposition for each needs to be clear with better links to registration for both.

Publisher and Advertiser sign up buttons should be on the home page.

I am leaving the brief open save I request that you use green colours on the template.

I want room to be able to add more tabs on the top level if we introduce a blog or other services.

The layout needs to be solid and please work with the copy that's already there.

see http://brightplacely.example

I am looking forward to reviewing your ideas and designs.
Updates

The button to carbon neutral cert I am going to want to make smaller and put it in the bottom of the site.

Do not go down the too fluffy green route with windmills and fuzzy clouds. I am looking for something simple, professional but also organic with a bit of zest to it. 

We are not a niche player serving ads to green only site with green only ads. We simply neutralise the effect of online advertising campaigns.

Some decent images in the header on rotation could work I am not sure. I think these would have to be abstract and largely if not totally green in colour.

Target Market(s)

BrightPlacely.com is an online ad network. Our targets are publishers and advertisers. We bring them together through providing ad serving to the network we have built on behalf of our advertisers.

Advertisers are agencys, brands, large companies looking to sell online or create awareness of the brand.

Requirements
Must have
• Please keep the site clean and use green and white
• Call to action to both publishers and advertisers to join (buttons on home page)

```html
<!DOCTYPE html>
<html lang="en">
<head>
<meta charset="utf-8">
<title>BrightPlacely.com – Advertising Network</title>
<link rel="stylesheet" href="https://fonts.googleapis.com/css2?family=Arimo:wght@400;700&display=swap">
<style>
:root{
  --green:#4c9a2a;
  --green-dark:#2f7a1a;
  --green-light:#7cc04f;
  --green-text:#3f8f1f;
  --grey-cell:#b9b9b9;
  --grey-cell-light:#cfcfcf;
  --text:#444;
  --text-dark:#333;
  --rule:#dcdcdc;
  --panel-bg:#f6f6f6;
  --white:#fff;
}
*{box-sizing:border-box;margin:0;padding:0}
html,body{width:864px;height:1200px;overflow:hidden;background:var(--white)}
body{font-family:"Arimo",Arial,sans-serif;color:var(--text);font-size:10px;line-height:1.3}
.canvas{position:relative;width:864px;height:1200px;overflow:hidden}
a{color:inherit;text-decoration:none}

/* header */
.site-header{position:absolute;left:0;top:0;width:864px;height:74px;border-bottom:1px solid var(--rule)}
.brand{position:absolute;left:62px;top:18px;display:flex;align-items:center;gap:8px;font-size:27px;font-weight:700;color:var(--green-dark);letter-spacing:-.5px}
.brand-dot{width:24px;height:24px;border-radius:50%;background:var(--green)}
.main-nav{position:absolute;right:76px;top:30px;display:flex;align-items:center;font-size:10px;color:var(--green-text)}
.main-nav a{padding:0 6px}
.main-nav .sep{color:#bbb}
.main-nav .active{background:var(--green-light);color:var(--white);border-radius:9px;padding:3px 7px}

/* sub nav */
.sub-nav{position:absolute;left:0;top:75px;width:864px;height:28px;background:linear-gradient(#fff,#eaeaea);display:flex;align-items:flex-end;padding-left:66px;font-size:10px;color:var(--text-dark)}
.sub-nav a{padding:0 8px 8px}
.sub-nav .sep{padding-bottom:8px}
.sub-nav .active{background:linear-gradient(var(--green-light),var(--green));color:var(--white);padding:9px 6px 8px;border-radius:3px 3px 0 0}

/* hero */
.hero{position:absolute;left:0;top:103px;width:864px;height:106px;background:linear-gradient(180deg,#6fb848 0%,#4f9e2c 100%);border-bottom:1px solid #3c8a1e}
.hero-art{position:absolute;right:80px;top:0;width:400px;height:106px;background:linear-gradient(90deg,rgba(255,255,255,0) 0%,rgba(40,120,30,.55) 55%,rgba(20,90,20,.7) 100%)}
.hero h1{position:absolute;left:66px;top:22px;font-size:22px;color:var(--white);font-weight:700}
.hero p{position:absolute;left:66px;top:54px;width:400px;font-size:10.5px;color:var(--white);line-height:1.25}

/* main column */
.content{position:absolute;left:62px;top:0;width:476px}
.section{position:absolute;left:0;width:476px}
.section-head{height:22px;padding:6px 0 0 6px;background:linear-gradient(#ececec,#fff);border-radius:4px 4px 0 0;font-size:10.5px;font-weight:700;color:var(--text-dark);display:flex;align-items:center;gap:4px}
.section-head svg{width:11px;height:11px}
.section p{margin-left:6px;width:462px;font-size:9.6px;line-height:1.35}
.section p+p{margin-top:12px}
.section strong{color:var(--text-dark)}
.green-link{color:var(--green-text);text-decoration:underline}

.channel-title{position:absolute;left:0;font-size:10.5px;font-weight:700;color:var(--green-text)}
.channel-grid{position:absolute;left:0;border-collapse:collapse;width:474px;font-size:9.8px;font-weight:700;color:var(--white)}
.channel-grid td{height:22.5px;padding-left:12px;border:1px solid #e5e5e5}
.channel-grid tr.grey td{background:linear-gradient(var(--grey-cell-light),var(--grey-cell))}
.channel-grid tr.green td{background:linear-gradient(var(--green-light),var(--green))}
.note{position:absolute;left:0;font-size:8.6px;font-style:italic;color:var(--text)}

.measure{position:absolute;left:10px;top:824px}
.measure h3{font-size:10.5px;font-weight:700;color:var(--text-dark);margin-bottom:3px}
.measure li{list-style:none;font-size:9.6px;display:flex;align-items:center;gap:4px;margin-left:4px}
.measure li::before{content:"";width:7px;height:7px;border-radius:50%;background:#555}

/* sidebar */
.panel{position:absolute;left:562px;width:225px;border:1px solid var(--rule);border-radius:4px;background:var(--white);box-shadow:0 2px 3px rgba(0,0,0,.06)}
.panel h2{height:30px;padding:9px 10px;font-size:11px;font-weight:700;color:var(--text-dark)}
.panel-body{margin:0 5px 5px;border:1px solid #e4e4e4;border-radius:3px;height:calc(100% - 36px);background:linear-gradient(#fff,var(--panel-bg));position:relative}
.panel-icon{position:absolute;left:7px;top:8px;width:60px;height:60px}
.panel-text{position:absolute;left:76px;top:8px;width:140px;font-size:9px;line-height:1.2;color:var(--text-dark)}
.panel-actions{position:absolute;left:75px;display:flex;gap:3px}
.pill{background:#6a6a6a;color:var(--white);font-size:9px;border-radius:9px;padding:3px 9px}
.blog-list{list-style:none;padding:4px 6px 0}
.blog-list li{padding:7px 0 5px;border-bottom:1px dotted #ccc;font-size:9px;color:var(--text-dark)}
.blog-list li:last-child{border-bottom:none}
.blog-list a{display:block;color:var(--green-text)}

/* footer */
.site-footer{position:absolute;left:0;top:1060px;width:864px;height:140px;background:linear-gradient(#e2e2e2,#f7f7f7 25%,#fff)}
.footer-col{position:absolute;top:16px;font-size:9px;color:var(--text-dark);line-height:1.55}
.footer-col h4{font-size:9.5px;font-weight:700;color:#555}
.footer-about{position:absolute;left:565px;top:13px;width:220px;font-size:9px;line-height:1.45;color:var(--text-dark)}
.footer-about h4{color:var(--green-text);font-size:9.5px}
.footer-rule{position:absolute;left:62px;top:92px;width:724px;border-top:1px solid #ddd}
.cert-badge{position:absolute;left:62px;top:98px;width:52px;height:34px;border-radius:17px;background:var(--green);opacity:.85}
.phones{position:absolute;left:157px;top:109px;font-size:11px;color:var(--green-dark)}
.phones b{font-weight:700}
</style>
</head>
<body>
<div class="canvas">

  <header class="site-header">
    <a class="brand" href="http://brightplacely.example"><span class="brand-dot"></span>BrightPlacely.com</a>
    <nav class="main-nav">
      <a href="#">Home</a>
      <a class="active" href="#">Advertisers</a>
      <a href="#">Publishers</a><span class="sep">|</span>
      <a href="#">Referral</a><span class="sep">|</span>
      <a href="#">Offsetting</a><span class="sep">|</span>
      <a href="#">Contact</a>
    </nav>
  </header>

  <nav class="sub-nav">
    <a class="active" href="#">Testimonials</a>
    <a href="#">Ad Formats</a><span class="sep">|</span>
    <a href="#">Advertiser Registration</a><span class="sep">|</span>
    <a href="#">Advertiser Agreement</a>
  </nav>

  <section class="hero">
    <div class="hero-art" role="img" aria-label="Abstract green arrows pointing right"></div>
    <h1>Advertising Network</h1>
    <p>Through BrightPlacely.com you can access hundreds of millions of advertising impressions across a range of high quality web sites.</p>
  </section>

  <main class="content">
    <section class="section" style="top:229px">
      <div class="section-head"><svg viewBox="0 0 12 12"><circle cx="6" cy="6" r="5.3" fill="#fff" stroke="#777"/><path d="M5 3.5 7.5 6 5 8.5" fill="none" stroke="#555" stroke-width="1.4"/></svg>Targeting</div>
      <p>BrightPlacely.com is a contextual advertising network, meaning the ads we serve are contextually relevant to the content of the page to increase relevance and campaign performance.</p>
      <p>We provide a range of targeting options to boost campaign performance including <strong>Behavioural Targeting, Re-Targeting, Geo-Targeting, Frequency Capping and Channel Targeting.</strong></p>
    </section>

    <section class="section" style="top:332px">
      <div class="section-head"><svg viewBox="0 0 12 12"><circle cx="6" cy="6" r="5.3" fill="#fff" stroke="#777"/><path d="M5 3.5 7.5 6 5 8.5" fill="none" stroke="#555" stroke-width="1.4"/></svg>Channels</div>
      <p>We offer both Business and Consumer Channels made up of sites we have reviewed and categorised to ensure high volumes of quality traffic.</p>
    </section>

    <h2 class="channel-title" style="top:391px">Top Level Business Channels</h2>
    <table class="channel-grid" style="top:410px">
      <tr class="grey"><td style="width:237px">General Business</td><td>E-Commerce</td></tr>
      <tr class="green"><td>Business Opportunities</td><td>Industrial Goods and Services</td></tr>
      <tr class="grey"><td>Business Services</td><td>Real Estate</td></tr>
      <tr class="green"><td>Construction &amp; Maintenance</td><td></td></tr>
    </table>

    <h2 class="channel-title" style="top:520px">Consumer Top Level Channels</h2>
    <table class="channel-grid" style="top:537px">
      <tr class="grey"><td style="width:143px">Arts</td><td style="width:178px">Reference</td><td>Regional</td></tr>
      <tr class="green"><td>Automotive</td><td>Home</td><td>Science</td></tr>
      <tr class="grey"><td>Computers</td><td>Internet</td><td>Shopping</td></tr>
      <tr class="green"><td>Games</td><td>Money and Finance</td><td>Society</td></tr>
      <tr class="grey"><td>Health</td><td>News</td><td>Sports</td></tr>
      <tr class="green"><td>Recreation</td><td>Kids and Teens</td><td></td></tr>
    </table>
    <p class="note" style="top:684px">* We have an incredible 174 channels and sub-channels available to target.</p>

    <section class="section" style="top:706px">
      <div class="section-head"><svg viewBox="0 0 12 12"><circle cx="6" cy="6" r="5.3" fill="#fff" stroke="#777"/><path d="M5 3.5 7.5 6 5 8.5" fill="none" stroke="#555" stroke-width="1.4"/></svg>Ad Formats</div>
      <p>BrightPlacely.com accept all IAB recognised ad formats. You can insert you own code into the creative to serve flash based or rich media ads.</p>
    </section>

    <section class="section" style="top:758px">
      <div class="section-head"><svg viewBox="0 0 12 12"><circle cx="6" cy="6" r="5.3" fill="#fff" stroke="#777"/><path d="M5 3.5 7.5 6 5 8.5" fill="none" stroke="#555" stroke-width="1.4"/></svg>Tags</div>
      <p>You can insert your own campaign tags into campaigns to so we pull them from you ad server or for campaign tracking in a 3rd party system.</p>
    </section>

    <div class="measure">
      <h3>Measurement &amp; Reporting</h3>
      <ul>
        <li>Real time campaign tracking and reporting</li>
        <li>Advanced ROI tracking</li>
        <li>Keyword Performance Reporting</li>
      </ul>
    </div>

    <section class="section" style="top:885px">
      <div class="section-head"><svg viewBox="0 0 12 12"><circle cx="6" cy="6" r="5.3" fill="#fff" stroke="#777"/><path d="M5 3.5 7.5 6 5 8.5" fill="none" stroke="#555" stroke-width="1.4"/></svg>Rates</div>
      <p>Our ad serving platform works on an exchange basis where advertisers bid for advertising impressions on our networks.</p>
      <p>Campaigns are bought in advance by credit card through PayKite or by emailing <a class="green-link" href="mailto:io@brightplacely.example">io@brightplacely.example</a> with a campaign brief and budget to place an insertion order and we will generate an invoice for payment.</p>
      <p>You should feel good in the assurance that by advertising with us all of your ads are carbon offset helping you meet your responsibilities as a business by reducing the carbon impact of your online advertising campaigns.</p>
    </section>
  </main>

  <aside>
    <div class="panel" style="top:228px;height:131px">
      <h2>Advertisers</h2>
      <div class="panel-body">
        <svg class="panel-icon" viewBox="0 0 60 60" aria-hidden="true"><circle cx="30" cy="30" r="29" fill="#5aa832"/><rect x="16" y="17" width="28" height="20" rx="1.5" fill="none" stroke="#fff" stroke-width="3"/><rect x="27" y="37" width="6" height="5" fill="#fff"/><rect x="21" y="42" width="18" height="3" fill="#fff"/></svg>
        <p class="panel-text">BrightPlacely.com can provide you access to over a billion impressions a month to drive quality traffic to your website to convert.</p>
        <div class="panel-actions" style="top:67px"><a class="pill" href="#">Register</a><a class="pill" href="#">Read more</a></div>
      </div>
    </div>

    <div class="panel" style="top:371px;height:130px">
      <h2>Publishers</h2>
      <div class="panel-body">
        <svg class="panel-icon" viewBox="0 0 60 60" aria-hidden="true"><circle cx="30" cy="30" r="29" fill="#5aa832"/><circle cx="30" cy="23" r="5" fill="#fff"/><path d="M21 40a9 9 0 0 1 18 0z" fill="#fff"/><circle cx="18" cy="27" r="4" fill="#fff"/><path d="M10 41a8 8 0 0 1 14-4v4z" fill="#fff"/><circle cx="42" cy="27" r="4" fill="#fff"/><path d="M50 41a8 8 0 0 0-14-4v4z" fill="#fff"/></svg>
        <p class="panel-text">We are always on the look out for new publishers to join our ad network and by joining us you are joining a network of aggregated content.</p>
        <div class="panel-actions" style="top:65px"><a class="pill" href="#">Register</a><a class="pill" href="#">Read more</a></div>
      </div>
    </div>

    <div class="panel" style="top:513px;height:153px">
      <h2>From Our Blog</h2>
      <div class="panel-body">
        <ul class="blog-list">
          <li><a href="#">4 reasons why people choose to share online</a>August 26th, 2010 by Tessa Morland</li>
          <li><a href="#">The kittens are coming to Bristol!</a>August 24th, 2010 by Jonah Brell</li>
          <li><a href="#">Blogger tips: How to write compelling blog posts</a>August 24th, 2010 by Rhea Colby</li>
        </ul>
      </div>
    </div>
  </aside>

  <footer class="site-footer">
    <div class="footer-col" style="left:64px"><h4>Pages</h4>Contact<br>Offsetting<br>Referral</div>
    <div class="footer-col" style="left:165px"><h4>Publishers</h4>Advertising Formats<br>Publisher Information<br>Publisher Login<br>Publisher Sign Up</div>
    <div class="footer-col" style="left:288px"><h4>Advertisers</h4>Advertiser Information<br>Advertiser Login<br>Advertiser Sign Up<br>Advertising Formats</div>
    <div class="footer-col" style="left:408px"><h4>Useful Info</h4>Terms &amp; Conditions : Advertisers<br>Terms &amp; Conditions : Publishers<br>User Guide: Advertisers<br>User Guide: Publishers</div>
    <div class="footer-about"><h4>Copyright BrightPlacely.com Ltd 2010</h4>BrightPlacely.com offers publishers to the opportunity to earn more income through text (inline text links) or by displaying targeted contextual advertising banner ads on their websites or blogs.</div>
    <div class="footer-rule"></div>
    <div class="cert-badge"></div>
    <p class="phones">347 555-0182 <b>USA</b> &nbsp;|&nbsp; 020 7946 0321 <b>UK</b> &nbsp;|&nbsp; 08-555 10 482 <b>Sweden</b> &nbsp;|&nbsp; 02 5550 1247 <b>Australia</b> &nbsp;|&nbsp; 21 5550193 <b>Hungary</b></p>
  </footer>

</div>
</body>
</html>
```